Photo-Video Combo Package Flyer

Need to create a flyer to showcase a combo package featuring photography and videography from two separate companies. I need an 8 1/2 X 11 flyer in .psd so I can make changes as needed as well as all fonts
Target Market(s)
Brides & Grooms
Industry/Entity Type
Wedding Photography
Requirements
Must have
- see word doc
Nice to have
- please visit websites for inspiration
- https://quietharborimages.com/
- www.kqbrt.com

```html
<!DOCTYPE html>
<html lang="en">
<head>
<meta charset="utf-8">
<title>Photo-Video Combo Package</title>
<link rel="stylesheet" href="https://fonts.googleapis.com/css2?family=Antonio:wght@300;400&family=Barlow+Semi+Condensed:wght@500;600;700&family=Cormorant+Garamond:ital,wght@0,500;1,500&family=Montserrat:wght@300;400&family=Roboto+Condensed:wght@300;400&family=Roboto:wght@400&display=swap">
<style>
  :root {
    --ink: #1b1b1b;
    --paper-top: #f2f3f3;
    --paper-mid: #d9dcdd;
    --white: #ffffff;
    --footer: #0b0b0b;
    --footer-text: #e8e8e8;
    --footer-muted: #a9a9a9;
    --box-line: #2a2a2a;
  }
  * { margin: 0; padding: 0; box-sizing: border-box; }
  html, body { width: 927px; height: 1200px; overflow: hidden; background: var(--white); }
  .flyer {
    position: relative; width: 927px; height: 1200px; overflow: hidden;
    background: radial-gradient(ellipse at 45% 55%, var(--paper-top) 0%, var(--paper-mid) 100%);
    font-family: "Roboto Condensed", sans-serif; color: var(--ink);
  }
  .hero {
    position: absolute; left: 0; top: 0; width: 927px; height: 472px;
    background: linear-gradient(180deg, #8a7fa3 0%, #d8a7a0 18%, #f2c08e 30%, #7b6f8d 45%, #4a4a5f 62%, #2e2a2c 100%);
  }
  .brand {
    position: absolute; left: 60px; top: 110px; width: 480px; text-align: center; color: var(--white);
  }
  .brand-name { font-family: "Cormorant Garamond", serif; font-weight: 500; font-size: 60px; line-height: 1; }
  .brand-sub { font-family: "Cormorant Garamond", serif; font-size: 17px; letter-spacing: 5px; margin-top: 14px; }
  .photo { position: absolute; }
  .photo-garden { left: 100px; top: 300px; width: 134px; height: 174px; background: linear-gradient(160deg, #2f3d26, #8c9a86 60%, #d9dde2); }
  .photo-camera { left: 302px; top: 260px; width: 306px; height: 306px; background: linear-gradient(135deg, #7e8ea3 0%, #2a2c31 45%, #101113 80%); }
  .photo-sunset { left: 208px; top: 434px; width: 168px; height: 155px; background: linear-gradient(180deg, #c9a58e 0%, #e9a06a 45%, #4b5e73 100%); }
  .photo-trees { left: 630px; top: 300px; width: 164px; height: 174px; background: radial-gradient(circle at 62% 20%, #fff7d8 0%, #d8a24e 15%, #3b3222 50%, #17140f 100%); }
  .photo-dock { left: 630px; top: 478px; width: 138px; height: 86px; background: linear-gradient(180deg, #6d8fc4 0%, #36508a 60%, #1f2b4a 100%); }
  .frame { position: absolute; border: 3px solid var(--white); }
  .frame-main { left: 286px; top: 236px; width: 342px; height: 348px; }
  .frame-side { left: 76px; top: 530px; width: 178px; height: 180px; }
  .title { position: absolute; left: 236px; top: 614px; width: 454px; text-align: center; }
  .title-main { font-family: "Antonio", sans-serif; font-weight: 400; font-size: 64px; line-height: 1; letter-spacing: 0.5px; }
  .title-sub { font-family: "Montserrat", sans-serif; font-weight: 300; font-size: 22px; letter-spacing: 11px; margin-top: 6px; }
  .intro {
    position: absolute; left: 82px; top: 732px; width: 353px;
    font-size: 19.5px; line-height: 28px; text-align: justify; font-weight: 300;
  }
  .offer { position: absolute; left: 82px; top: 962px; display: flex; align-items: center; gap: 18px; }
  .offer-num { font-family: "Antonio", sans-serif; font-weight: 300; font-size: 92px; line-height: 1; }
  .offer-text { font-family: "Antonio", sans-serif; font-weight: 300; font-size: 40px; line-height: 38px; }
  .price { position: absolute; left: 466px; top: 726px; width: 420px; font-family: "Barlow Semi Condensed", sans-serif; font-weight: 600; }
  .price-line { display: flex; align-items: baseline; gap: 18px; font-size: 24px; }
  .price-amount { font-size: 32px; font-weight: 700; }
  .price-save { font-size: 20px; margin-top: 2px; }
  .package {
    position: absolute; top: 794px; height: 239px; border: 2px solid var(--box-line);
    padding: 8px 10px; font-family: "Roboto", sans-serif; font-size: 12px; line-height: 13px;
  }
  .package-photo { left: 466px; width: 237px; }
  .package-video { left: 714px; width: 166px; }
  .package h3 { font-family: "Barlow Semi Condensed", sans-serif; font-weight: 500; font-size: 15px; margin-bottom: 9px; }
  .package li { list-style: none; margin-bottom: 13px; }
  .package-photo li { margin-bottom: 12.5px; }
  .partner { position: absolute; left: 776px; top: 1080px; display: flex; align-items: center; gap: 5px; font-family: "Roboto Condensed", sans-serif; font-weight: 400; font-size: 12px; }
  .partner-dot { width: 9px; height: 9px; border-radius: 50%; background: var(--ink); }
  .footer { position: absolute; left: 0; top: 1122px; width: 927px; height: 78px; background: var(--footer); color: var(--footer-text); }
  .note { position: absolute; top: 15px; display: flex; align-items: center; gap: 10px; font-family: "Roboto", sans-serif; font-size: 9.5px; line-height: 13px; }
  .note svg { width: 38px; height: 38px; flex: none; }
  .note-contact { left: 42px; }
  .note-photo { left: 184px; }
  .note-video { left: 315px; }
  .contact { position: absolute; top: 12px; font-family: "Montserrat", sans-serif; }
  .contact-photo { left: 495px; }
  .contact-video { left: 718px; }
  .contact-label { font-size: 7.5px; letter-spacing: 2px; color: var(--footer-muted); }
  .contact-phone { font-size: 21px; font-weight: 300; letter-spacing: 3.5px; margin: 2px 0 3px; }
  .contact-web { font-size: 7.5px; letter-spacing: 2px; color: var(--footer-muted); text-transform: uppercase; }
</style>
</head>
<body>
<main class="flyer">
  <div class="hero" role="img" aria-label="Bride and groom embracing on a ship deck at sunset over the sea"></div>
  <div class="brand">
    <div class="brand-name">Quiet Harbor</div>
    <div class="brand-sub">IMAGES</div>
  </div>

  <div class="frame frame-main"></div>
  <div class="frame frame-side"></div>
  <div class="photo photo-garden" role="img" aria-label="Couple kissing on a bench in a garden at night"></div>
  <div class="photo photo-trees" role="img" aria-label="Sun shining through trees at dusk"></div>
  <div class="photo photo-camera" role="img" aria-label="Camera lens with a bride holding a bouquet on its screen"></div>
  <div class="photo photo-sunset" role="img" aria-label="Couple kissing on the beach at sunset"></div>
  <div class="photo photo-dock" role="img" aria-label="Couple standing on a dock at twilight"></div>

  <div class="title">
    <div class="title-main">THE PHOTO-VIDEO</div>
    <div class="title-sub">COMBO PACKAGE</div>
  </div>

  <p class="intro">is the best way to hire your Photographer and videographer. Both companies are highly rated by The Vow Guide and Aisle Reviews as well as recommended by the area’s top wedding venues. When your photographer and videographer are working together your wedding day will run smoothly, so you can just enjoy yourself and have fun!</p>

  <div class="offer">
    <div class="offer-num">10%</div>
    <div class="offer-text">OFF ANY<br>UPGRADES</div>
  </div>

  <div class="price">
    <div class="price-line"><span>PHOTO VIDEO COMBO PRICE</span><span class="price-amount">$2999</span></div>
    <div class="price-save">$750 SAVINGS</div>
  </div>

  <section class="package package-photo">
    <h3>Photo Package Includes</h3>
    <ul>
      <li>1 Hr Engagement Shoot</li>
      <li>One photographer up to 7 hours<br>on location for wedding</li>
      <li>High Resolution, Edited digital images</li>
      <li>Images professionally edited in house</li>
      <li>Beautiful online gallery to download from</li>
      <li>Print release to print at the lab<br>of your choice</li>
      <li>Normal Retail Price $2450</li>
    </ul>
  </section>
  <section class="package package-video">
    <h3>Video Package Includes</h3>
    <ul>
      <li>Up To 6 Hours of Coverage</li>
      <li>Documentary Style Video<br>Edit 60-90 Minutes</li>
      <li>Edited Background Music</li>
      <li>A Cinematic highlight<br>Recap 3-4 minutes</li>
      <li>3 Personalized DVDs</li>
      <li>Normal retail Price $1299</li>
    </ul>
  </section>

  <div class="partner"><span class="partner-dot"></span>Kestrel Bright Video</div>

  <footer class="footer">
    <div class="note note-contact">
      <svg viewBox="0 0 38 38" fill="none" stroke="#e8e8e8" stroke-width="1.2"><circle cx="19" cy="19" r="18"/><path d="M13 11c-2 1-2 4 0 8s6 8 9 9c2 0 3-1 4-2l-3-3-2 1c-2-1-4-4-5-6l1-2-3-4z"/></svg>
      <span>Contact us to learn<br>more and schedule<br>a consultation.</span>
    </div>
    <div class="note note-photo">
      <svg viewBox="0 0 38 38" fill="none" stroke="#e8e8e8" stroke-width="1.2"><circle cx="19" cy="19" r="18"/><rect x="10" y="14" width="18" height="12" rx="1.5"/><path d="M15 14l1.5-2.5h5L23 14"/><circle cx="19" cy="20" r="3.5"/></svg>
      <span>Photography<br>provided by Quiet<br>Harbor Images</span>
    </div>
    <div class="note note-video">
      <svg viewBox="0 0 38 38" fill="none" stroke="#e8e8e8" stroke-width="1.2"><circle cx="19" cy="19" r="18"/><rect x="10" y="16" width="13" height="10" rx="1"/><path d="M23 19l5-3v10l-5-3"/><circle cx="13" cy="13" r="2.5"/><circle cx="19" cy="13" r="2.5"/></svg>
      <span>Videography<br>provided by Kestrel<br>Bright Video</span>
    </div>
    <div class="contact contact-photo">
      <div class="contact-label">PHOTO CONTACT INFO</div>
      <div class="contact-phone">555-210-4863</div>
      <div class="contact-web">quietharborimages.com</div>
    </div>
    <div class="contact contact-video">
      <div class="contact-label">VIDEO CONTACT INFO</div>
      <div class="contact-phone">555-307-2294</div>
      <div class="contact-web">www.kqbrt.com</div>
    </div>
  </footer>
</main>
</body>
</html>
```